Trade Show Booth Sign Design for Retracting Banner

I need a trade show booth sign designed. It will be for a retractable banner that is double sided with 34 by 81 inch.

I want to incorporate my logo (see attached, have it in other file formats as well) and graphics from my website (https://www.dolbrookteachingadvisory.com/) with parts or all of the following text.

· Educational Content Creation
o Supplemental Textbook Content Development
o E-learning Content Development
· Curriculum Development
o KVTR/Bright Ladder
o Three Dimensional Learning
· Assessment
o Formative Assessments
o Elementary School, Middle School, High School, College, and Business
· Professional Development
o Training
o Facilitation

Target Market(s)

Education

Industry/Entity Type

Education

Font styles to use
Sans Serif

Colors

Designer to choose colors to be used in the design.

Requirements
Must have
• Eye catching and easy to read design
Nice to have
• Would like to see incorporation of my logo and some of the elements of my website images
Should not have
• N/A

```html
<!DOCTYPE html>
<html lang="en">
<head>
<meta charset="utf-8">
<title>Dolbrook Teaching Advisory – Banner</title>
<link rel="stylesheet" href="https://fonts.googleapis.com/css2?family=Roboto+Condensed:wght@400;700&display=swap">
<style>
  :root{
    --navy:#1d2b6e;
    --blue:#29a9dc;
    --band:#1c78bd;
    --green:#8cc640;
    --gold:#f7a928;
    --orange:#f26a22;
    --ink:#1d2b4f;
    --white:#ffffff;
    --paper:#f4f5f6;
  }
  *{box-sizing:border-box;margin:0;padding:0}
  html,body{width:1200px;height:2866px;overflow:hidden;background:var(--white)}
  body{font-family:"Roboto Condensed",Arial,sans-serif;color:var(--ink);position:relative}

  .brand{position:absolute;left:0;top:0;width:1200px;height:360px;text-align:center;color:var(--navy);font-weight:700}
  .brand-name{display:block;font-size:250px;line-height:1;letter-spacing:-4px;margin-top:18px}
  .brand-sub{display:block;font-size:76px;line-height:1;margin-top:2px}

  .photo-band{position:absolute;left:0;width:1200px}
  .photo-top{top:372px;height:458px;background:radial-gradient(circle at 50% 45%,#4a4a4a 0,#2a2a2a 55%,#1f1f1f 100%)}
  .photo-bottom{top:2678px;height:188px;background:radial-gradient(circle at 50% 40%,#454545 0,#262626 70%)}

  .rule{position:absolute;left:0;top:842px;width:1200px;height:26px;background:var(--band)}

  .panel{position:absolute;left:0;top:868px;width:1200px;height:1662px;background:var(--paper)}
  .frames{position:absolute;left:0;top:868px}

  .quad{position:absolute;width:460px}
  .quad h2{font-size:58px;line-height:1;font-weight:700;text-transform:uppercase;margin-bottom:24px}
  .quad ul{list-style:none}
  .quad li{position:relative;padding-left:62px;font-size:42px;line-height:1.1;margin-bottom:18px;color:var(--ink)}
  .quad li::before{content:"";position:absolute;left:0;top:8px;width:36px;height:36px;border:4px solid var(--navy);background:var(--white)}
  .quad li::after{content:"";position:absolute;left:12px;top:2px;width:14px;height:30px;border-right:7px solid var(--navy);border-bottom:7px solid var(--navy);transform:rotate(40deg)}

  .q-content{left:96px;top:1140px}
  .q-content h2{color:var(--blue)}
  .q-assess{left:660px;top:1140px}
  .q-assess h2{color:var(--green)}
  .q-curric{left:96px;top:1985px}
  .q-curric h2{color:var(--gold)}
  .q-prof{left:660px;top:1985px}
  .q-prof h2{color:var(--orange)}

  .url-band{position:absolute;left:0;top:2530px;width:1200px;height:148px;background:var(--band);color:var(--white);font-size:66px;font-weight:700;text-align:center;line-height:148px}
</style>
</head>
<body>

<header class="brand">
  <span class="brand-name">DOLBROOK</span>
  <span class="brand-sub">Teaching Advisory</span>
</header>

<div class="photo-band photo-top" role="img" aria-label="Photo of crumpled colourful paper balls around a glowing yellow light bulb on a dark chalkboard"></div>
<div class="rule"></div>
<div class="panel"></div>

<svg class="frames" width="1200" height="1662" viewBox="0 0 1200 1662" aria-hidden="true">
  <g fill="none" stroke-width="12" stroke-linecap="round">
    <path d="M80 200 V820 Q80 860 120 860 H540 Q580 860 580 820 V150 Q580 110 540 110 H230" stroke="var(--blue)"/>
    <path d="M970 110 H660 Q620 110 620 150 V820 Q620 860 660 860 H1080 Q1120 860 1120 820 V200" stroke="var(--green)"/>
    <path d="M80 1040 V1590 Q80 1630 120 1630 H540 Q580 1630 580 1590 V990 Q580 950 540 950 H230" stroke="var(--gold)"/>
    <path d="M970 950 H660 Q620 950 620 990 V1590 Q620 1630 660 1630 H1080 Q1120 1630 1120 1590 V1040" stroke="var(--orange)"/>
  </g>

  <!-- Educational content hex -->
  <g transform="translate(150 130)">
    <polygon points="0,-100 87,-50 87,50 0,100 -87,50 -87,-50" fill="var(--blue)"/>
    <g fill="none" stroke="var(--white)" stroke-width="6" stroke-linejoin="round">
      <path d="M-45 -32 Q-20 -40 0 -28 Q20 -40 45 -32 V34 Q20 26 0 38 Q-20 26 -45 34 Z"/>
      <path d="M0 -28 V38"/>
      <path d="M-34 -14 H-12 M-34 0 H-12 M-34 14 H-12 M12 -14 H34 M12 0 H34 M12 14 H34" stroke-width="4"/>
    </g>
  </g>

  <!-- Assessment hex -->
  <g transform="translate(1050 130)">
    <polygon points="0,-100 87,-50 87,50 0,100 -87,50 -87,-50" fill="var(--green)"/>
    <g fill="none" stroke="var(--white)" stroke-width="6" stroke-linejoin="round">
      <rect x="-40" y="-38" width="60" height="76"/>
      <path d="M-28 -20 H8 M-28 -4 H8 M-28 12 H-4" stroke-width="4"/>
      <path d="M40 -30 L50 -20 L10 24 L-2 28 L2 16 Z"/>
    </g>
  </g>

  <!-- Curriculum hex -->
  <g transform="translate(150 970)">
    <polygon points="0,-100 87,-50 87,50 0,100 -87,50 -87,-50" fill="var(--gold)"/>
    <g fill="none" stroke="var(--white)" stroke-width="6" stroke-linejoin="round">
      <path d="M10 -36 H-40 V38 H34 V-6"/>
      <path d="M38 -42 L48 -32 L6 12 L-8 16 L-4 2 Z"/>
    </g>
  </g>

  <!-- Professional development hex -->
  <g transform="translate(1050 970)">
    <polygon points="0,-100 87,-50 87,50 0,100 -87,50 -87,-50" fill="var(--orange)"/>
    <g fill="none" stroke="var(--white)" stroke-width="6" stroke-linejoin="round">
      <path d="M0 -34 L54 -10 L0 14 L-54 -10 Z"/>
      <path d="M-30 2 V28 Q0 44 30 28 V2"/>
      <path d="M46 -6 V26"/>
    </g>
  </g>
</svg>

<section class="quad q-content">
  <h2>Educational<br>Content</h2>
  <ul>
    <li>Supplemental Textbook</li>
    <li>Content Development</li>
    <li>E-learning Content Development</li>
  </ul>
</section>

<section class="quad q-assess">
  <h2>Assessment<br>Development</h2>
  <ul>
    <li>Formative Assessments</li>
    <li>Elementary School, Middle School, High School, College &amp; Business</li>
  </ul>
</section>

<section class="quad q-curric">
  <h2>Curriculum<br>Development</h2>
  <ul>
    <li>KVTR/ Bright Ladder</li>
    <li>Three Dimensional Learning</li>
  </ul>
</section>

<section class="quad q-prof">
  <h2>Professional<br>Development</h2>
  <ul>
    <li>Training</li>
    <li>Facilitation</li>
  </ul>
</section>

<div class="url-band">www.dolbrookteachingadvisory.com</div>

<div class="photo-band photo-bottom" role="img" aria-label="Photo of crumpled colourful paper balls and light bulbs on a dark background"></div>

</body>
</html>
```